KESTREL Communications Business Card- Belsa

Kestrel Integrated Communications is Corporate communications agency with more than 20 years of experience. We become part of the manegement team of our clients in other to improve their outcomes and grow the possitioning of their brand.
We are in Puerto Rico, latin caribbean island
Name: Maribelsa (Belsa) Ocampo
787-555-0148
bocampo@kestrelwing.example

Target Market(s)

finance and pharmaceutical companies

Industry/Entity Type

Business

Contact Information for Business Card

modern, edgy colorful and playfull like our logo

Requirements
Must have
• company logo
• name
• tel
• email

```html
<!DOCTYPE html>
<html lang="en">
<head>
<meta charset="utf-8">
<title>Kestrel Integrated Communications – Business Card</title>
<link href="https://fonts.googleapis.com/css2?family=Open+Sans:wght@400;600;700&display=swap" rel="stylesheet">
<style>
  :root {
    --bg: #2b2b2b;
    --brown: #3d3120;
    --orange: #f05a22;
    --ink: #2e2a24;
    --paper: #ffffff;
    --rule: #3a3228;
  }
  * { box-sizing: border-box; margin: 0; padding: 0; }
  html, body { width: 1200px; height: 900px; overflow: hidden; }
  body {
    background: var(--bg);
    font-family: "Open Sans", Arial, sans-serif;
    position: relative;
  }
  .card {
    position: absolute;
    left: 320px;
    width: 560px;
    height: 320px;
    overflow: hidden;
    box-shadow: 0 10px 30px rgba(0,0,0,.45);
  }
  .card--back { top: 60px; background: var(--brown); }
  .card--front { top: 500px; background: var(--paper); }

  .wordmark {
    font-family: "Open Sans", Arial, sans-serif;
    font-weight: 700;
    letter-spacing: .08em;
    line-height: 1.25;
    text-transform: uppercase;
    display: flex;
    align-items: center;
    gap: 10px;
  }
  .wordmark__dot { width: 14px; height: 14px; border-radius: 50%; background: currentColor; flex: none; }

  .card--back .wordmark {
    position: absolute; left: 0; right: 0; top: 0; bottom: 0;
    justify-content: center;
    color: var(--paper);
    font-size: 22px;
    text-align: center;
  }

  .card--front .wordmark {
    position: absolute; left: 34px; top: 92px;
    color: var(--ink);
    font-size: 15px;
  }

  .holder {
    position: absolute; right: 34px; top: 118px;
    color: var(--orange);
    font-weight: 700;
    font-size: 19px;
    letter-spacing: .02em;
    text-transform: uppercase;
  }
  .rule { position: absolute; height: 1px; background: var(--rule); }
  .rule--name { left: 250px; right: 30px; top: 150px; }
  .rule--contact { left: 30px; width: 230px; top: 232px; }

  .contact {
    position: absolute; left: 34px; top: 242px;
    list-style: none;
    color: var(--ink);
    font-size: 13px;
    line-height: 1.6;
  }
  .contact li { display: flex; align-items: center; gap: 7px; }
  .contact svg { width: 11px; height: 11px; flex: none; }

  .wave { position: absolute; left: 0; bottom: 0; width: 560px; height: 320px; }
</style>
</head>
<body>
  <section class="card card--back" aria-label="Card back">
    <div class="wordmark"><span class="wordmark__dot"></span><span>Kestrel<br>Integrated Communications</span></div>
  </section>

  <section class="card card--front" aria-label="Card front">
    <svg class="wave" viewBox="0 0 560 320" aria-hidden="true">
      <path d="M230 320 C380 300 430 150 560 150 L560 320 Z" fill="var(--orange)"/>
      <path d="M250 320 C395 305 440 162 560 162 L560 320 Z" fill="var(--brown)"/>
    </svg>

    <div class="wordmark"><span class="wordmark__dot"></span><span>Kestrel<br>Integrated<br>Communications</span></div>

    <p class="holder">Maribelsa (Belsa) Ocampo</p>
    <div class="rule rule--name"></div>
    <div class="rule rule--contact"></div>

    <ul class="contact">
      <li>
        <svg viewBox="0 0 24 24"><path fill="var(--orange)" d="M6.6 10.8a15 15 0 0 0 6.6 6.6l2.2-2.2a1 1 0 0 1 1-.25 11.4 11.4 0 0 0 3.6.57 1 1 0 0 1 1 1V20a1 1 0 0 1-1 1A17 17 0 0 1 3 4a1 1 0 0 1 1-1h3.5a1 1 0 0 1 1 1c0 1.25.2 2.45.57 3.57a1 1 0 0 1-.25 1z"/></svg>
        787-555-0148
      </li>
      <li>
        <svg viewBox="0 0 24 24"><rect x="2" y="5" width="20" height="14" rx="1" fill="none" stroke="var(--orange)" stroke-width="2"/><path d="M2 6l10 7 10-7" fill="none" stroke="var(--orange)" stroke-width="2"/></svg>
        bocampo@kestrelwing.example
      </li>
    </ul>
  </section>
</body>
</html>
```